New Business Card & Logo Design Project for PR Agency

Halvery & Associates Tech Public Relations agency is looking for a new business card design. Please see our website at www.halvery-pr.example for a description of our services. The design does not necessarily have to match the website’s aesthetic as we are looking for something fresh and modern that reflects our business. We want to emphasize that our focus is on media & public relations, content creation, social media and SEO. We want the business card to convey our BtoB technology focus and should have a very clean look. You are welcome to draw from our current halvery & associates logo on the card or play with that design too. We also like the idea of utilizing blue and white, which are often used in technology-related designs and layouts.
Attached are jpegs of the current logo and current card design for your reference.
Target Market(s)
Our clients are Business-to-Business technology providers.We sell our services to the CEO/President/Marketing director of a technology providing company.
Industry/Entity Type
Business
Look and feel

```html
<!DOCTYPE html>
<html lang="en">
<head>
<meta charset="utf-8">
<title>Halvery &amp; Associates – Business Card Options</title>
<link rel="stylesheet" href="https://fonts.googleapis.com/css2?family=Tinos:wght@400;700&display=swap">
<style>
  :root {
    --board: #5b2c16;
    --card-blue: #3889b0;
    --accent-blue: #3a86ad;
    --ink-dark: #3a3d40;
    --ink-grey: #62666a;
    --paper: #ffffff;
    --label: #ffffff;
    --serif: "Tinos", "Times New Roman", serif;
  }
  * { margin: 0; padding: 0; box-sizing: border-box; }
  html, body { width: 1200px; height: 843px; overflow: hidden; }
  body { background: var(--board); font-family: var(--serif); position: relative; }

  .option-label {
    position: absolute; top: 24px; width: 562px;
    text-align: center; color: var(--label);
    font-size: 62px; font-weight: 400; line-height: 1;
  }
  .option-label--one { left: 14px; }
  .option-label--two { left: 622px; }

  .card {
    position: absolute; width: 562px; height: 302px;
    box-shadow: 3px 5px 8px rgba(0,0,0,.45);
  }
  .card--front { top: 126px; background: var(--card-blue); text-align: center; }
  .card--front-one { left: 14px; }
  .card--front-two { left: 622px; }

  .front-wordmark {
    position: absolute; left: 0; right: 0; top: 128px;
    font-size: 47px; line-height: 1;
  }
  .front-tagline {
    position: absolute; left: 0; right: 0; top: 190px;
    font-size: 24px; line-height: 1;
  }
  .card--front-one .front-wordmark,
  .card--front-one .front-tagline { color: var(--ink-dark); }
  .card--front-two .front-wordmark,
  .card--front-two .front-tagline { color: var(--paper); }

  .card--back { left: 295px; top: 492px; background: var(--paper); }
  .back-rule-vertical {
    position: absolute; left: 47px; top: 0; width: 2px; height: 112px;
    background: var(--accent-blue);
  }
  .back-rule-horizontal {
    position: absolute; left: 395px; right: 0; top: 130px; height: 2px;
    background: var(--accent-blue);
  }
  .back-wordmark {
    position: absolute; right: 26px; top: 35px;
    font-size: 33px; line-height: 1; color: var(--ink-grey);
  }
  .holder-name {
    position: absolute; left: 38px; top: 128px;
    font-size: 23px; line-height: 1; color: var(--accent-blue);
  }
  .holder-title {
    position: absolute; left: 38px; top: 155px;
    font-size: 14px; line-height: 1; font-weight: 700; color: var(--ink-grey);
  }
  .contact {
    position: absolute; display: flex; align-items: center; gap: 8px;
    font-size: 15px; color: var(--ink-grey); white-space: nowrap;
  }
  .contact--address { font-size: 13px; }
  .contact svg { width: 18px; height: 18px; flex: none; }
  .contact--phone { left: 35px; top: 230px; }
  .contact--web { left: 35px; top: 259px; }
  .contact--email { left: 238px; top: 230px; }
  .contact--address { left: 238px; top: 259px; }
  .back-band {
    position: absolute; left: 0; right: 0; bottom: 0; height: 13px;
    background: var(--accent-blue);
  }
</style>
</head>
<body>
  <h2 class="option-label option-label--one">Option #1</h2>
  <h2 class="option-label option-label--two">Option #2</h2>

  <section class="card card--front card--front-one">
    <p class="front-wordmark">halvery &amp; associates</p>
    <p class="front-tagline">a public relations company</p>
  </section>

  <section class="card card--front card--front-two">
    <p class="front-wordmark">halvery &amp; associates</p>
    <p class="front-tagline">a public relations company</p>
  </section>

  <section class="card card--back">
    <div class="back-rule-vertical"></div>
    <p class="back-wordmark">halvery &amp; associates</p>
    <div class="back-rule-horizontal"></div>
    <p class="holder-name">Daniel Reyes</p>
    <p class="holder-title">Partner</p>

    <p class="contact contact--phone">
      <svg viewBox="0 0 18 18" aria-hidden="true"><rect width="18" height="18" rx="3" fill="#3a86ad"/><path d="M5 4c1 0 1.6 2 1.6 2.6 0 .6-.9 1-.9 1.4.5 1.5 1.8 2.8 3.3 3.3.4 0 .8-.9 1.4-.9.6 0 2.6.6 2.6 1.6 0 .9-1 1.8-2 1.8C7.5 13.8 4.2 10.5 3.2 6 3.2 5 4 4 5 4z" fill="#fff"/></svg>
      (555) 014-2290
    </p>
    <p class="contact contact--web">
      <svg viewBox="0 0 18 18" aria-hidden="true"><rect width="18" height="18" rx="3" fill="#3a86ad"/><circle cx="9" cy="9" r="5.5" fill="none" stroke="#fff" stroke-width="1.3"/><ellipse cx="9" cy="9" rx="2.3" ry="5.5" fill="none" stroke="#fff" stroke-width="1.1"/><path d="M3.5 9h11" stroke="#fff" stroke-width="1.1"/></svg>
      www.halvery-pr.example
    </p>
    <p class="contact contact--email">
      <svg viewBox="0 0 18 18" aria-hidden="true"><rect width="18" height="18" rx="3" fill="#3a86ad"/><rect x="3.5" y="5" width="11" height="8" fill="none" stroke="#fff" stroke-width="1.3"/><path d="M3.5 5l5.5 4.5L14.5 5" fill="none" stroke="#fff" stroke-width="1.3"/></svg>
      dreyes@halvery-pr.example
    </p>
    <p class="contact contact--address">
      <svg viewBox="0 0 18 18" aria-hidden="true"><rect width="18" height="18" rx="3" fill="#3a86ad"/><path d="M9 3.5l6 5.5h-1.8v5.5H10.5v-3.5h-3v3.5H4.8V9H3z" fill="#fff"/></svg>
      48 Harbor Lane, Suite 3, Brookfield, Ohio 00000
    </p>
    <div class="back-band"></div>
  </section>
</body>
</html>
```